Business card New design- upscale

Looking for modern design business cards. Minimalist, mix of gloss and matte finishes. Texas based Contractor company doing Mechanical hvac and plumbing, focused on commercial and industrial manufacturing facilities. We don't hand too many out so high end materials or functionality...will be considered. Please see attached files for info needed on cards. *New plumbing license needs to be edited to say M82716. Www.polvaxgroup.com
P.s. Website will also be redesigned soon.

Target Market(s)

Facility managers for commercial buildings, mechanical engineers for industrial manufacturing facilities including pharmaceutical, semiconductor, food & beverage, etc

Contact Information for Business Card

See attached images

Requirements
Must have
• All Logo colors: purple, black and Gray. 1, 2 or 4 rounded corners. All content on existing business cards (see attached images).
Nice to have
• Matte and gloss print. Embossing, raised print, functionality.
Should not have
• Stock images, generic construction.

```html
<!DOCTYPE html>
<html lang="en">
<head>
<meta charset="utf-8">
<title>Polvax Group – Business Card</title>
<link href="https://fonts.googleapis.com/css2?family=Poppins:wght@400;500;600;700;800&display=swap" rel="stylesheet">
<style>
  :root {
    --purple: #4d2d6b;
    --purple-deep: #3b1f57;
    --charcoal: #3f3f3f;
    --white: #ffffff;
    --ink: #1f1f1f;
    --backdrop: #e9e9e9;
  }
  * { box-sizing: border-box; margin: 0; padding: 0; }
  html, body { width: 1200px; height: 800px; overflow: hidden; }
  body {
    background: var(--backdrop);
    font-family: "Poppins", sans-serif;
    position: relative;
  }
  .card {
    position: absolute;
    top: 68px;
    width: 380px;
    height: 665px;
    border-radius: 22px;
    overflow: hidden;
    background: var(--white);
    box-shadow: 0 10px 30px rgba(0,0,0,0.18);
  }
  .card--front { left: 170px; }
  .card--back { left: 650px; }

  .card__shapes { position: absolute; inset: 0; }

  .brand {
    position: absolute;
    top: 92px;
    left: 0; right: 0;
    display: flex;
    align-items: center;
    justify-content: center;
    gap: 12px;
    color: var(--purple-deep);
    font-weight: 700;
    font-size: 34px;
    letter-spacing: 2px;
  }
  .brand__mark {
    width: 22px; height: 22px;
    background: var(--purple-deep);
  }

  .contact {
    position: absolute;
    top: 300px;
    left: 0; right: 0;
    text-align: center;
    color: var(--white);
  }
  .contact__name { font-size: 31px; font-weight: 800; line-height: 1.1; }
  .contact__title { font-size: 14px; font-weight: 400; margin-top: 4px; }
  .contact__lines { margin-top: 16px; font-size: 16px; line-height: 1.35; }
  .contact__rule {
    width: 250px; height: 1px; margin: 10px auto;
    background: var(--white);
  }
  .contact__services { font-size: 14px; line-height: 1.35; }

  .web-band {
    position: absolute;
    left: 0; right: 0; bottom: 0;
    height: 58px;
    display: flex; align-items: center; justify-content: center;
    color: var(--white);
    font-size: 17px;
    letter-spacing: 0.5px;
  }
  .web-band--front { background: var(--charcoal); }
  .web-band--back { background: var(--purple); font-weight: 600; font-size: 22px; }

  .regulation {
    position: absolute;
    top: 46px; left: 0; right: 0;
    text-align: center;
    color: var(--ink);
    font-size: 17px;
    line-height: 1.55;
    padding: 0 20px;
  }
</style>
</head>
<body>

  <section class="card card--front" aria-label="Business card front">
    <svg class="card__shapes" width="380" height="665" viewBox="0 0 380 665" aria-hidden="true">
      <path d="M0 205 C 120 200, 200 215, 260 260 C 300 290, 340 300, 380 300 L380 665 L0 665 Z" fill="var(--purple)"/>
      <path d="M0 190 C 120 186, 205 200, 265 248 C 305 280, 345 292, 380 292" fill="none" stroke="var(--purple)" stroke-width="3"/>
    </svg>

    <div class="brand">
      <span class="brand__mark"></span>
      <span class="brand__name">POLVAX GROUP</span>
    </div>

    <div class="contact">
      <p class="contact__name">Dale Hartwell</p>
      <p class="contact__title">Lead Estimator/Sr. Project Manager</p>
      <div class="contact__lines">
        <p>Call:(520) 555-0147</p>
        <p>Office:(817) 555-0192</p>
        <p>dhartwell@polvaxgroup.com</p>
      </div>
      <div class="contact__rule"></div>
      <div class="contact__lines">
        <p>2180 Cedar Ridge Rd.</p>
        <p>Granbury, TX 76048</p>
      </div>
      <div class="contact__rule"></div>
      <div class="contact__services">
        <p>Commercial &amp; Industrail Contractors</p>
        <p>Mechanical &amp; Plumbing Services</p>
      </div>
    </div>

    <div class="web-band web-band--front">WWW.POLVAXGROUP.COM</div>
  </section>

  <section class="card card--back" aria-label="Business card back">
    <div class="regulation">
      <p>RMP - M82716 Regulated BY</p>
      <p>THE Lone Star Board Of</p>
      <p>Plumbing Examiners,</p>
      <p>P.O. Box 3100,</p>
      <p>Austin, TX. 78700;</p>
      <p>1-800-555-0163,</p>
      <p>512-555-0128</p>
      <p>TACLA58210C</p>
      <p>regulated by the Lone Star</p>
      <p>Department of Licensing and</p>
      <p>Regulation, P.O. Box 10440,</p>
      <p>Austin, TX. 78710;</p>
      <p>1-800-555-0176,</p>
      <p>512-555-0139</p>
    </div>
    <div class="web-band web-band--back">www.lsdlr-board.org</div>
  </section>

</body>
</html>
```